Creative, Colorful, Dynamic Infographic for Global Non-Profit

We are a global arts and education non-profit in need of an infographic that illustrates four key skills embedded in our work: Curiosity, Listening, Imagination, Postive Action.
We work primarily with educators, students, and artists who use the power of personal stories to build community and connection and to bridge divides.
Our new brand guidelines, logos, and fonts are here: https://stylekit.example/lanternfold-9
I've attached a mock-up of the graphic and the required text. (Note the attached design was created by a staff person, your final design does not need to be the same. The color scheme and text of the final design should match the brand guidelines above.)
The graphic will be used for both web and print media and should include the purple Lanternfold 9 logo (also attached).
Ideally the final design will delight audiences and spark interest in our work.

```html
<!DOCTYPE html>
<html lang="en">
<head>
<meta charset="utf-8">
<title>Lanternfold 9 — Four Skills</title>
<link rel="stylesheet" href="https://fonts.googleapis.com/css2?family=IBM+Plex+Sans:wght@400;600&display=swap">
<style>
  :root {
    --red: #ee4444;
    --purple: #663397;
    --blue: #226abf;
    --yellow: #e8c945;
    --ink: #333333;
    --paper: #fdfdfd;
    --white: #ffffff;
  }
  html, body {
    margin: 0;
    padding: 0;
    width: 1200px;
    height: 1200px;
    overflow: hidden;
    background: var(--paper);
  }
  .skills-graphic {
    display: block;
    width: 1200px;
    height: 1200px;
    font-family: "IBM Plex Sans", Arial, sans-serif;
  }
  .petal-red, .quad-red, .ring-red, .box-red { fill: var(--red); }
  .petal-purple, .quad-purple, .ring-purple, .box-purple, .brand-disc { fill: var(--purple); }
  .petal-blue, .quad-blue, .ring-blue, .box-blue { fill: var(--blue); }
  .petal-yellow, .quad-yellow, .ring-yellow, .box-yellow { fill: var(--yellow); }
  .gap, .ring-inner, .arrow { fill: var(--white); }
  .skill-text { fill: var(--ink); font-size: 33px; text-anchor: middle; }
  .skill-title { font-weight: 600; }
  .petal-text { font-size: 31px; text-anchor: middle; fill: var(--white); }
  .petal-text.on-yellow { fill: var(--ink); }
  .brand-name { fill: var(--white); font-size: 34px; font-weight: 600; text-anchor: middle; }
</style>
</head>
<body>
<svg class="skills-graphic" viewBox="0 0 1932 1932" xmlns="http://www.w3.org/2000/svg" role="img" aria-label="Four skills cycle: Curiosity, Listening, Imagination, Positive action">
  <defs>
    <clipPath id="clip-top"><rect x="0" y="0" width="1932" height="643"/></clipPath>
    <clipPath id="clip-bottom"><rect x="0" y="1289" width="1932" height="643"/></clipPath>
    <clipPath id="clip-left"><rect x="0" y="0" width="640" height="1932"/></clipPath>
    <clipPath id="clip-right"><rect x="1292" y="0" width="640" height="1932"/></clipPath>
  </defs>

  <!-- petals -->
  <ellipse class="petal-purple" cx="966" cy="620" rx="245" ry="315" clip-path="url(#clip-top)"/>
  <ellipse class="petal-blue" cx="966" cy="1312" rx="245" ry="315" clip-path="url(#clip-bottom)"/>
  <ellipse class="petal-red" cx="620" cy="966" rx="315" ry="245" clip-path="url(#clip-left)"/>
  <ellipse class="petal-yellow" cx="1312" cy="966" rx="315" ry="245" clip-path="url(#clip-right)"/>

  <!-- centre quadrants -->
  <rect class="quad-red" x="757" y="757" width="209" height="221"/>
  <rect class="quad-purple" x="966" y="757" width="211" height="221"/>
  <rect class="quad-blue" x="757" y="978" width="209" height="199"/>
  <rect class="quad-yellow" x="966" y="978" width="211" height="199"/>

  <!-- skill rings -->
  <g class="skill-ring">
    <circle class="gap" cx="699" cy="699" r="250"/>
    <circle class="ring-red" cx="699" cy="699" r="234"/>
    <circle class="ring-inner" cx="699" cy="699" r="203"/>
  </g>
  <g class="skill-ring">
    <circle class="gap" cx="1234" cy="699" r="250"/>
    <circle class="ring-purple" cx="1234" cy="699" r="234"/>
    <circle class="ring-inner" cx="1234" cy="699" r="203"/>
  </g>
  <g class="skill-ring">
    <circle class="gap" cx="699" cy="1233" r="250"/>
    <circle class="ring-blue" cx="699" cy="1233" r="234"/>
    <circle class="ring-inner" cx="699" cy="1233" r="203"/>
  </g>
  <g class="skill-ring">
    <circle class="gap" cx="1234" cy="1233" r="250"/>
    <circle class="ring-yellow" cx="1234" cy="1233" r="234"/>
    <circle class="ring-inner" cx="1234" cy="1233" r="203"/>
  </g>

  <!-- arrow boxes -->
  <rect class="box-purple" x="960" y="652" width="125" height="92" rx="18"/>
  <path class="arrow" d="M990,698 L1018,670 L1030,682 L1018,690 L1054,690 L1054,706 L1018,706 L1030,714 L1018,726 Z"/>

  <rect class="box-red" x="654" y="849" width="92" height="125" rx="18"/>
  <path class="arrow" d="M700,944 L672,916 L684,904 L692,916 L692,880 L708,880 L708,916 L716,904 L728,916 Z"/>

  <rect class="box-blue" x="848" y="1185" width="125" height="92" rx="18"/>
  <path class="arrow" d="M944,1231 L916,1259 L904,1247 L916,1239 L879,1239 L879,1223 L916,1223 L904,1215 L916,1203 Z"/>

  <rect class="box-yellow" x="1189" y="958" width="92" height="125" rx="18"/>
  <path class="arrow" d="M1235,988 L1263,1016 L1251,1028 L1243,1016 L1243,1052 L1227,1052 L1227,1016 L1219,1028 L1207,1016 Z"/>

  <!-- brand mark -->
  <circle class="gap" cx="966" cy="968" r="125"/>
  <circle class="brand-disc" cx="966" cy="968" r="116"/>
  <text class="brand-name" x="966" y="980">Lanternfold 9</text>

  <!-- petal text -->
  <text class="petal-text">
    <tspan x="968" y="415">Your positive actions</tspan>
    <tspan x="968" y="458">lead to curiosity</tspan>
    <tspan x="968" y="500">about what else</tspan>
    <tspan x="968" y="543">is possible</tspan>
  </text>
  <text class="petal-text">
    <tspan x="465" y="934">Your curiosity</tspan>
    <tspan x="465" y="977">allows you</tspan>
    <tspan x="465" y="1019">to listen</tspan>
  </text>
  <text class="petal-text on-yellow">
    <tspan x="1492" y="934">Your imagination</tspan>
    <tspan x="1492" y="977">can spark</tspan>
    <tspan x="1492" y="1019">positive action</tspan>
  </text>
  <text class="petal-text">
    <tspan x="968" y="1438">Your listening</tspan>
    <tspan x="968" y="1481">allows you to</tspan>
    <tspan x="968" y="1523">take in new</tspan>
    <tspan x="968" y="1566">information</tspan>
  </text>

  <!-- skill text -->
  <text class="skill-text">
    <tspan class="skill-title" x="699" y="625">Curiosity –</tspan>
    <tspan x="699" y="668">Focus on how you can</tspan>
    <tspan x="699" y="710">learn from another's</tspan>
    <tspan x="699" y="753">knowledge and</tspan>
    <tspan x="699" y="795">experience</tspan>
  </text>
  <text class="skill-text">
    <tspan class="skill-title" x="1245" y="625">Positive action -</tspan>
    <tspan x="1245" y="668">Show your words</tspan>
    <tspan x="1245" y="710">and actions</tspan>
    <tspan x="1245" y="753">matter</tspan>
  </text>
  <text class="skill-text">
    <tspan class="skill-title" x="697" y="1178">Listening –</tspan>
    <tspan x="697" y="1221">Seek to</tspan>
    <tspan x="697" y="1264">understand</tspan>
    <tspan x="697" y="1306">before speaking</tspan>
  </text>
  <text class="skill-text">
    <tspan class="skill-title" x="1234" y="1178">Imagination –</tspan>
    <tspan x="1234" y="1221">Consider</tspan>
    <tspan x="1234" y="1264">possibilities beyond</tspan>
    <tspan x="1234" y="1306">what you know</tspan>
  </text>
</svg>
</body>
</html>
```